Business Card Design Project

We need a simple business card design that uses our current logo.
We need to have the current logo put into a high res format.
We need to have 1 card made with contact information.
We will supply the information for the 4 employees.
Industry/Entity Type
Business
Requirements
Must have
- The contact information is as follows:
Mark Dellweather
Producer/CEO
c. 949-555-0147
f. 650-555-0193
markd@lanternbay.example
Al Vostrand, CFO
c. 949-555-0162
f. 650-555-0193
alv@lanternbay.example
Peter Malvane, PR
c. 267-555-0128
f. 650-555-0193
pmalvane@lanternbay.example
Tim Garrowby, Producer
c. 949-555-0184
f. 650-555-0193
timg@lanternbay.example
The address for all cards is:
318 W Calle Norvento #2715, San Clemente, CA 92681

```html
<!DOCTYPE html>
<html lang="en">
<head>
<meta charset="utf-8">
<title>Business Card Sample</title>
<link rel="stylesheet" href="https://fonts.googleapis.com/css2?family=Arimo:wght@400;700&family=Great+Vibes&display=swap">
<style>
  :root {
    --page: #ffffff;
    --panel-top: #1f2122;
    --panel-mid: #000000;
    --panel-bottom: #1c1e1f;
    --card-black: #000000;
    --card-grey: #2a2b2c;
    --brand-blue: #4fa8e6;
    --brand-blue-deep: #2f88cc;
    --title-white: #e9e9e9;
    --text-white: #f2f2f2;
    --address-grey: #6f6f6f;
    --card-white: #ffffff;
    --icon-box: #2b2d30;
    --droplet-tone: rgba(120, 120, 120, 0.18);
  }
  * { margin: 0; padding: 0; box-sizing: border-box; }
  html, body {
    width: 910px;
    height: 1200px;
    overflow: hidden;
    background: var(--page);
  }
  .sheet {
    position: absolute;
    left: 9px; top: 11px;
    width: 890px; height: 1178px;
    border-radius: 6px;
    background: linear-gradient(to bottom, var(--panel-top) 0%, #141516 30%, var(--panel-mid) 52%, #050505 75%, var(--panel-bottom) 100%);
    box-shadow: 0 0 3px rgba(0,0,0,0.6);
  }
  .sheet-title {
    position: absolute;
    left: 0; top: 14px;
    width: 100%;
    text-align: center;
    font-family: "Great Vibes", cursive;
    font-size: 78px;
    color: var(--title-white);
    text-shadow: 0 2px 3px rgba(0,0,0,0.8);
  }
  .card {
    position: absolute;
    left: 100px;
    width: 698px;
    height: 393px;
    border-radius: 10px;
    overflow: hidden;
    box-shadow: 0 2px 4px rgba(0,0,0,0.5);
  }
  .card--front { top: 221px; background: var(--card-white); }
  .card--back {
    top: 694px;
    background: linear-gradient(to bottom, #3a3b3c 0%, var(--card-grey) 25%, #111 60%, var(--card-black) 100%);
  }
  .front-face {
    position: absolute;
    left: 0; top: 0;
    width: 100%; height: 292px;
    background: linear-gradient(to bottom, var(--card-black) 0%, #0b0c0d 55%, #202325 100%);
    border-bottom: 2px solid var(--brand-blue-deep);
  }
  .droplets {
    position: absolute;
    left: 0; top: 0;
    width: 330px; height: 100%;
    background: radial-gradient(ellipse at 40% 40%, var(--droplet-tone), rgba(0,0,0,0) 70%);
  }
  .brand-name {
    position: absolute;
    right: 38px;
    font-family: "Arimo", sans-serif;
    font-weight: 700;
    font-size: 33px;
    letter-spacing: 0.5px;
    color: var(--brand-blue);
    white-space: nowrap;
  }
  .card--front .brand-name { top: 24px; }
  .card--back .brand-name { top: 322px; }
  .person-name, .person-role {
    position: absolute;
    left: 292px; width: 390px;
    text-align: center;
    font-family: "Arimo", sans-serif;
    font-weight: 700;
    text-transform: uppercase;
    white-space: nowrap;
  }
  .person-name {
    top: 101px;
    font-size: 16px;
    letter-spacing: 8px;
    color: var(--brand-blue);
  }
  .person-role {
    top: 133px;
    font-size: 12px;
    letter-spacing: 9px;
    color: var(--text-white);
  }
  .contact-list {
    position: absolute;
    left: 358px; top: 203px;
    list-style: none;
    font-family: "Arimo", sans-serif;
    font-size: 15px;
    color: var(--text-white);
  }
  .contact-list li {
    display: flex;
    align-items: center;
    height: 27.5px;
  }
  .contact-icon {
    display: inline-flex;
    align-items: center;
    justify-content: center;
    width: 18px; height: 18px;
    margin-right: 9px;
    background: var(--icon-box);
    color: var(--brand-blue);
    font-size: 13px;
    border-radius: 2px;
  }
  .address {
    position: absolute;
    left: 0; top: 345px;
    width: 100%;
    text-align: center;
    font-family: "Arimo", sans-serif;
    font-size: 20px;
    letter-spacing: 0.6px;
    color: var(--address-grey);
  }
  .view-label {
    position: absolute;
    left: 0; width: 100%;
    text-align: center;
    font-family: "Great Vibes", cursive;
    font-size: 20px;
    color: var(--brand-blue-deep);
  }
  .view-label--front { top: 625px; }
  .view-label--back { top: 1103px; }
</style>
</head>
<body>
  <main class="sheet">
    <h1 class="sheet-title">Business Card Sample</h1>

    <section class="card card--front">
      <div class="front-face">
        <div class="droplets" role="img" aria-label="Scattered silver water droplets"></div>
        <div class="brand-name">LANTERN BAY MEDIA</div>
        <div class="person-name">Mark Dellweather</div>
        <div class="person-role">Producer / CEO</div>
        <ul class="contact-list">
          <li><span class="contact-icon">c</span>949-555-0147</li>
          <li><span class="contact-icon">f</span>650-555-0193</li>
          <li><span class="contact-icon">e</span>markd@lanternbay.example</li>
        </ul>
      </div>
      <p class="address">318 W Calle Norvento #2715, San Clemente, CA 92681</p>
    </section>
    <p class="view-label view-label--front">Front View</p>

    <section class="card card--back">
      <div class="droplets" role="img" aria-label="Scattered silver water droplets"></div>
      <div class="brand-name">LANTERN BAY MEDIA</div>
    </section>
    <p class="view-label view-label--back">Back View</p>
  </main>
</body>
</html>
```